Real Estate Development Firm
Project: Real Estate Development Firm
Real Estate Development Firm - Real Estate
Creative Brief
Professional
Pavel Lorent
Pavel@HarborlineGroup.com
www.HarborlineGroup.com
On the Bottom of the business card (footer) I would like to list Development * Construction * Management * Real Estate * Lending
Just the logo

```html
<!DOCTYPE html>
<html lang="en">
<head>
<meta charset="utf-8">
<title>Harborline Group – Business Card</title>
<link rel="stylesheet" href="https://fonts.googleapis.com/css2?family=Montserrat:wght@600;700&family=Cabin:wght@400;500&display=swap">
<style>
  :root {
    --backdrop: #3d3d3d;
    --card-white: #f5f5f5;
    --brand-blue: #15518f;
    --brand-blue-deep: #0b3f7c;
    --brand-blue-bright: #0a8ad8;
    --text-grey: #4a4a4a;
    --rule-grey: #b9bec4;
    --white: #ffffff;
  }
  * { margin: 0; padding: 0; box-sizing: border-box; }
  html, body {
    width: 1200px; height: 750px; overflow: hidden;
    background: var(--backdrop);
  }
  .canvas { position: relative; width: 1200px; height: 750px; }

  .card {
    position: absolute; top: 218px;
    width: 492px; height: 282px;
    border-radius: 15px; overflow: hidden;
  }

  /* Front */
  .card--front { left: 91px; background: var(--card-white); }
  .front-brand {
    position: absolute; left: 60px; top: 86px; width: 142px;
    display: flex; flex-direction: column; align-items: center; gap: 10px;
  }
  .brand-square {
    width: 40px; height: 40px; background: var(--brand-blue);
  }
  .brand-name {
    font-family: "Montserrat", sans-serif; font-weight: 700;
    font-size: 19px; line-height: 1.1; letter-spacing: 1px;
    color: var(--brand-blue); text-align: center; text-transform: uppercase;
  }

  .contact-block { position: absolute; left: 226px; top: 84px; }
  .person-name {
    font-family: "Montserrat", sans-serif; font-weight: 700;
    font-size: 19px; letter-spacing: 0.6px; color: var(--brand-blue);
    text-transform: uppercase; margin-bottom: 10px;
  }
  .contact-list { list-style: none; }
  .contact-item {
    display: flex; align-items: center; gap: 7px; height: 19px;
    font-family: "Cabin", sans-serif; font-size: 13px; color: var(--text-grey);
  }
  .contact-icon { width: 13px; height: 13px; flex: none; fill: var(--brand-blue); }

  .front-footer {
    position: absolute; left: 0; bottom: 0; width: 100%; height: 34px;
    border-top: 2px solid var(--rule-grey);
  }
  .front-footer__band {
    position: absolute; left: 0; right: 0; top: 3px; bottom: 0;
    background: linear-gradient(90deg, var(--brand-blue-deep) 0%, var(--brand-blue-bright) 50%, var(--brand-blue-deep) 100%);
    display: flex; align-items: center; justify-content: center;
    font-family: "Cabin", sans-serif; font-size: 12.5px; letter-spacing: 0.2px;
    color: var(--white); text-transform: uppercase; white-space: nowrap;
  }
  .service-dot { margin: 0 4px; }

  /* Back */
  .card--back {
    left: 620px;
    background: radial-gradient(ellipse at 50% 40%, #0b8edb 0%, #0a67b4 40%, #0b4a90 80%, #0a3f7e 100%);
  }
  .back-brand {
    position: absolute; left: 0; right: 0; top: 70px;
    display: flex; flex-direction: column; align-items: center; gap: 18px;
  }
  .back-brand .brand-square { width: 64px; height: 64px; background: var(--white); }
  .back-brand .brand-name { font-size: 30px; letter-spacing: 2px; color: var(--white); }
</style>
</head>
<body>
<main class="canvas">

  <section class="card card--front" aria-label="Business card front">
    <div class="front-brand">
      <span class="brand-square" aria-hidden="true"></span>
      <p class="brand-name">Harborline<br>Group</p>
    </div>

    <div class="contact-block">
      <h1 class="person-name">Pavel Lorent</h1>
      <ul class="contact-list">
        <li class="contact-item">
          <svg class="contact-icon" viewBox="0 0 13 13" aria-label="Mobile"><path d="M3.5 0h6a1 1 0 0 1 1 1v11a1 1 0 0 1-1 1h-6a1 1 0 0 1-1-1V1a1 1 0 0 1 1-1zm.5 1.5v8.5h5V1.5zM6.5 10.6a.8.8 0 1 0 0 1.6.8.8 0 0 0 0-1.6z"/></svg>
          555-214-7380
        </li>
        <li class="contact-item">
          <svg class="contact-icon" viewBox="0 0 13 13" aria-label="Fax"><path d="M3 0h7v3.5H3zM1 4.5h11a1 1 0 0 1 1 1V10h-2V8H2v2H0V5.5a1 1 0 0 1 1-1zM3 9h7v4H3z"/></svg>
          555-214-7391
        </li>
        <li class="contact-item">
          <svg class="contact-icon" viewBox="0 0 13 13" aria-label="Email"><path d="M0 2.5h13v1L6.5 7.5 0 3.5zM0 5l6.5 4L13 5v5.5H0z"/></svg>
          Pavel@HarborlineGroup.com
        </li>
        <li class="contact-item">
          <svg class="contact-icon" viewBox="0 0 13 13" aria-label="Website"><path d="M6.5 0a6.5 6.5 0 1 0 0 13 6.5 6.5 0 0 0 0-13zm0 1.1c.6.6 1.2 1.9 1.4 3.6H5.1C5.3 3 5.9 1.7 6.5 1.1zM4 4.7H1.5a5.4 5.4 0 0 1 3.3-3.3C4.4 2.2 4.1 3.4 4 4.7zm0 1.1c0 .5 0 1 .1 1.5H1.2a5.4 5.4 0 0 1 0-1.5zm1.1 0h2.8a9 9 0 0 1-.1 1.5H5.2a9 9 0 0 1-.1-1.5zm4 0h2.7a5.4 5.4 0 0 1 0 1.5H9c.1-.5.1-1 .1-1.5zm-.1-1.1c-.1-1.3-.4-2.5-.8-3.3a5.4 5.4 0 0 1 3.3 3.3zM1.5 8.4H4.2c.2 1.3.5 2.4.9 3.2A5.4 5.4 0 0 1 1.5 8.4zm3.8 0h2.4c-.3 1.6-.8 2.9-1.2 3.5-.4-.6-.9-1.9-1.2-3.5zm3.5 0h2.7a5.4 5.4 0 0 1-3.6 3.2c.4-.8.7-1.9.9-3.2z"/></svg>
          www.HarborlineGroup.com
        </li>
      </ul>
    </div>

    <footer class="front-footer">
      <div class="front-footer__band">
        Development<span class="service-dot">●</span>Construction<span class="service-dot">●</span>Management<span class="service-dot">●</span>Real Estate<span class="service-dot">●</span>Lending
      </div>
    </footer>
  </section>

  <section class="card card--back" aria-label="Business card back">
    <div class="back-brand">
      <span class="brand-square" aria-hidden="true"></span>
      <p class="brand-name">Harborline Group</p>
    </div>
  </section>

</main>
</body>
</html>
```